One page website for a Personal Injury Law Firm

Design and code a one page website in WordPress for the Darrow Law Firm, which is a a personal injury law firm located in Coral Gables, Florida. Please note: if you want to change the color pallete for the logo and for the web design , that is fine by me.

Target Market(s)

Those injured in accidents that need legal representation

Industry/Entity Type

Legal

Coding

Coded - Design and coding required

Number of Pages Required

1 page

Font styles to use
Other font styles liked:
• Montserrat

```html
<!DOCTYPE html>
<html lang="en">
<head>
<meta charset="utf-8">
<title>Darrow Law Firm | Personal Injury Attorneys in Coral Gables</title>
<link href="https://fonts.googleapis.com/css2?family=Montserrat:wght@400;500;600;700;800&family=Roboto:wght@400;500;700&display=swap" rel="stylesheet">
<style>
:root{
  --tan:#c5955e;
  --tan-dark:#b3824c;
  --ink:#1e1e1e;
  --text:#3a3a3a;
  --muted:#555;
  --grey-bg:#efefef;
  --white:#fff;
  --line:#d9d9d9;
}
*{box-sizing:border-box;margin:0;padding:0}
html,body{width:1200px;height:4823px;overflow:hidden}
body{font-family:"Roboto",Arial,sans-serif;color:var(--text);background:var(--white);position:relative}
.abs{position:absolute}
h1,h2,h3,h4,.mont{font-family:"Montserrat",Arial,sans-serif}
.btn{display:inline-flex;align-items:center;justify-content:center;background:var(--tan);color:var(--white);font-family:"Montserrat",Arial,sans-serif;font-weight:700;text-transform:uppercase;letter-spacing:.5px}
.rule{width:52px;height:3px;background:var(--tan)}

/* header */
.site-header{position:absolute;top:0;left:0;width:1200px;height:125px;background:var(--white)}
.brand{left:112px;top:30px;display:flex;align-items:center;gap:12px}
.brand-square{width:30px;height:30px;border:2px solid var(--tan)}
.brand-name{font-family:"Montserrat",Arial,sans-serif;font-weight:700;font-size:28px;color:var(--ink);line-height:1}
.contact-chip{display:flex;align-items:center;gap:16px;top:13px}
.chip-icon{width:40px;height:40px;border-radius:50%;background:var(--ink);display:flex;align-items:center;justify-content:center}
.chip-label{font-family:"Montserrat",Arial,sans-serif;font-size:12px;font-weight:600;color:var(--ink);text-transform:uppercase}
.chip-value{font-size:16px;color:var(--tan);margin-top:3px}
.nav-bar{left:0;top:71px;width:1200px;height:54px}
.nav{left:520px;top:71px;height:54px;display:flex;align-items:center;font-family:"Montserrat",Arial,sans-serif;font-size:15px;font-weight:500;color:var(--white);text-transform:uppercase}
.nav a{color:var(--white);text-decoration:none;position:absolute;white-space:nowrap}
.nav a.active{color:var(--ink);font-weight:700}

/* hero */
.hero{left:0;top:125px;width:1200px;height:600px}
.hero-title{left:0;width:1200px;top:312px;text-align:center;font-size:48px;font-weight:800;color:var(--white);letter-spacing:1px}
.hero-sub{left:0;width:1200px;top:381px;text-align:center;font-family:"Montserrat",Arial,sans-serif;font-weight:700;font-size:17px;color:var(--white);text-transform:uppercase}
.hero-btn{left:526px;top:430px;width:148px;height:42px;font-size:15px}

/* about */
.about-title{left:627px;top:813px;font-size:31px;font-weight:700;color:var(--ink)}
.about-rule{left:627px;top:860px}
.about-sub{left:627px;top:870px;font-size:22px;font-weight:600;color:var(--ink)}
.about-copy{left:627px;top:912px;width:460px;font-size:14.5px;line-height:31px;color:var(--text)}
.about-copy p+p{margin-top:31px}
.about-btn{left:627px;top:1303px;width:154px;height:43px;font-size:15px}

/* why */
.why{left:0;top:1458px;width:1200px;height:652px;background:linear-gradient(180deg,#c99a64,#c3915a)}
.why-title{left:0;width:1200px;top:1536px;text-align:center;font-size:31px;font-weight:700;color:var(--white)}
.why-rule{left:574px;top:1584px;background:var(--white)}
.why-sub{left:0;width:1200px;top:1598px;text-align:center;font-size:17px;color:var(--white)}
.why-card{top:1649px;width:305px;height:346px;background:var(--white);text-align:center;padding:0 22px}
.why-card .hex{position:absolute;left:117px;top:22px}
.why-card h3{position:absolute;left:0;width:100%;top:127px;font-size:19px;font-weight:500;line-height:30px;color:var(--ink)}
.why-card p{position:absolute;left:28px;right:28px;top:198px;font-size:14px;line-height:30px;color:var(--muted)}
.view-more{position:absolute;left:0;width:100%;top:296px;font-family:"Montserrat",Arial,sans-serif;font-weight:600;font-size:15px;color:var(--ink);display:flex;justify-content:center;align-items:center;gap:10px}

/* strategy */
.section-title{left:0;width:1200px;text-align:center;font-size:31px;font-weight:700;color:var(--ink)}
.section-sub{left:0;width:1200px;text-align:center;color:var(--ink)}
.strat-item{left:112px;width:466px}
.strat-item h4{position:absolute;left:99px;top:0;font-size:17.5px;font-weight:600;color:var(--ink)}
.strat-item p{position:absolute;left:99px;top:32px;width:360px;font-size:14.5px;line-height:28px;color:var(--text)}
.strat-item svg{position:absolute;left:0;top:-8px}
.strat-divider{left:112px;width:466px;height:1px;background:#cfcfcf}

/* practice */
.practice{left:0;top:2836px;width:1200px;height:824px;background:var(--grey-bg)}
.pa-card{width:225px;height:248px;background:var(--white);border:1px solid var(--line);text-align:center}
.pa-card.featured{background:var(--ink);border-color:var(--ink)}
.pa-card svg{position:absolute;left:82px;top:22px}
.pa-card h4{position:absolute;left:0;width:100%;top:80px;font-size:17px;font-weight:600;color:var(--ink)}
.pa-card.featured h4,.pa-card.featured p{color:var(--white)}
.pa-card p{position:absolute;left:14px;right:14px;top:112px;font-size:13.5px;line-height:24px;color:var(--muted)}
.pa-card .btn{position:absolute;left:58px;top:196px;width:108px;height:28px;font-size:13px;text-transform:none;font-family:"Roboto",Arial,sans-serif}

/* law */
.law-box{top:3866px;height:301px;background:var(--white);border:1px solid var(--line)}
.law-box.raised{box-shadow:0 6px 18px rgba(0,0,0,.14);border-color:#e6e6e6}
.law-head{height:107px;background:var(--ink);color:var(--white);padding:28px 30px 0 32px;font-size:19px;line-height:33px}
.law-head.tan{background:var(--tan)}
.law-list{list-style:none;padding:26px 30px 0 34px}
.law-list li{position:relative;padding-left:20px;font-size:14.5px;line-height:29px;color:var(--text);margin-bottom:27px}
.law-list li::before{content:"";position:absolute;left:0;top:11px;width:8px;height:8px;border-radius:50%;background:var(--ink)}
.law-list.tan-dots li::before{background:var(--tan)}

/* cta */
.cta{left:0;top:4278px;width:1200px;height:505px;background:var(--ink);color:var(--white)}
.cta-title{left:0;width:1200px;top:4356px;text-align:center;font-size:32px;font-weight:600;color:var(--white)}
.cta-sub{left:0;width:1200px;top:4414px;text-align:center;font-size:18px;font-weight:500;color:var(--white)}
.cta-note{left:0;width:1200px;top:4448px;text-align:center;font-size:14px;color:var(--white)}
.cta-col{top:4510px;width:380px;text-align:center;color:var(--white)}
.cta-col .label{display:flex;justify-content:center;align-items:center;gap:14px;font-size:16px}
.cta-col .ic{width:44px;height:44px;border-radius:50%;background:#3a3a3a;display:flex;align-items:center;justify-content:center}
.cta-col .ic span{width:30px;height:30px;border-radius:50%;background:var(--tan);display:flex;align-items:center;justify-content:center}
.cta-col .value{margin-top:22px;font-size:16px;line-height:29px}
.cta-divider{top:4512px;width:1px;height:84px;background:#777}
.cta-line{left:0;width:1200px;text-align:center;font-size:16px;color:var(--white)}
.site-footer{left:0;top:4783px;width:1200px;height:40px;background:var(--tan);color:var(--white);font-size:16px;text-align:center;line-height:40px}
</style>
</head>
<body>

<!-- Header -->
<header class="site-header">
  <div class="abs brand">
    <span class="brand-square"></span>
    <span class="brand-name">Darrow Law Firm</span>
  </div>
  <div class="abs contact-chip" style="left:509px">
    <span class="chip-icon"><svg width="18" height="14" viewBox="0 0 18 14"><rect x="1" y="1" width="16" height="12" rx="1.5" fill="none" stroke="#fff" stroke-width="1.8"/><path d="M1.5 2 9 8l7.5-6" fill="none" stroke="#fff" stroke-width="1.8"/></svg></span>
    <div><div class="chip-label">Send an email</div><div class="chip-value">hello@darrowinjurylaw.com</div></div>
  </div>
  <div class="abs contact-chip" style="left:835px">
    <span class="chip-icon"><svg width="18" height="18" viewBox="0 0 24 24"><path fill="#fff" d="M6.6 10.8a15 15 0 0 0 6.6 6.6l2.2-2.2a1 1 0 0 1 1-.25 11.4 11.4 0 0 0 3.6.6 1 1 0 0 1 1 1V20a1 1 0 0 1-1 1A17 17 0 0 1 3 4a1 1 0 0 1 1-1h3.5a1 1 0 0 1 1 1c0 1.25.2 2.45.6 3.6a1 1 0 0 1-.25 1z"/></svg></span>
    <div><div class="chip-label">Call for free consultation</div><div class="chip-value">305-555-0182</div></div>
  </div>
  <svg class="abs nav-bar" width="1200" height="54" viewBox="0 0 1200 54"><polygon points="466,0 1200,0 1200,54 440,54" fill="var(--tan)"/></svg>
  <nav class="abs nav">
    <a class="active" style="left:0">Home</a>
    <a style="left:94px">Area of Practice</a>
    <a style="left:296px">Reviews</a>
    <a style="left:414px">Contact</a>
    <a style="left:534px">Articles</a>
  </nav>
</header>

<!-- Hero -->
<section>
  <svg class="abs hero" width="1200" height="600" viewBox="0 0 1200 600">
    <defs>
      <linearGradient id="heroSky" x1="0" y1="0" x2="0" y2="1">
        <stop offset="0" stop-color="#3c4e6e"/>
        <stop offset=".45" stop-color="#5b5f76"/>
        <stop offset=".75" stop-color="#2d3445"/>
        <stop offset="1" stop-color="#1b2130"/>
      </linearGradient>
    </defs>
    <polygon points="0,0 1200,0 1200,488 600,580 0,488" fill="var(--tan)"/>
    <polygon points="0,0 1200,0 1200,480 600,570 0,480" fill="var(--ink)"/>
    <polygon role="img" aria-label="Downtown city skyline at dusk across the waterfront" points="0,0 1200,0 1200,470 600,558 0,470" fill="url(#heroSky)"/>
    <rect x="590" y="506" width="20" height="30" rx="10" fill="none" stroke="#fff" stroke-width="2"/>
    <line x1="600" y1="513" x2="600" y2="520" stroke="#fff" stroke-width="2"/>
  </svg>
  <h1 class="abs hero-title">THE DARROW LAW FIRM</h1>
  <p class="abs hero-sub">Concierge-level personal injury representation in Miami, Florida</p>
  <a class="abs btn hero-btn">Contact Us</a>
</section>

<!-- About -->
<section>
  <div class="abs" style="left:127px;top:823px;width:407px;height:506px;border:2px solid var(--ink)"></div>
  <div class="abs" role="img" aria-label="Attorneys meeting around a conference table" style="left:112px;top:842px;width:403px;height:347px;background:linear-gradient(135deg,#6f7780,#b9b4a8 55%,#8a8a86)"></div>
  <div class="abs" style="left:329px;top:1104px;width:225px;height:240px;background:var(--tan)"></div>
  <div class="abs" role="img" aria-label="Portrait of the lead attorney" style="left:352px;top:1058px;width:204px;height:267px;background:linear-gradient(180deg,#e9e9e9,#b9b9b9 60%,#3b3b3b)"></div>

  <h2 class="abs about-title">Justice. Recovery.</h2>
  <div class="abs rule about-rule"></div>
  <h3 class="abs about-sub">A Better Future Starts Here.</h3>
  <div class="abs about-copy">
    <p>At The <b>Darrow Law Firm</b>, we understand that suffering a personal injury can be life-altering—physically, emotionally, and financially. You may be unsure whether pursuing legal action is the right step. But in Florida, holding negligent parties accountable isn't just your right—it's often necessary to rebuild your life.</p>
    <p>We take a concierge-style approach to <b>personal injury law</b>, offering personalized attention, strategic advocacy, and relentless dedication to securing the maximum compensation you deserve. Our mission is not only to make you whole again but to help you build a brighter future—ensuring access to the best medical care, financial stability, and peace of mind for you and your loved ones.</p>
  </div>
  <a class="abs btn about-btn">Learn More</a>
</section>

<!-- Why choose -->
<section>
  <div class="abs why" role="img" aria-label="Warm tan overlay on office background"></div>
  <h2 class="abs why-title">Why Choose The Darrow Law Firm?</h2>
  <div class="abs rule why-rule"></div>
  <p class="abs why-sub">Unmatched Experience. Proven Results. Relentless Advocacy.</p>

  <article class="abs why-card" style="left:110px">
    <svg class="hex" width="70" height="76" viewBox="0 0 70 76"><polygon points="35,2 67,20 67,56 35,74 3,56 3,20" fill="none" stroke="var(--ink)" stroke-width="3"/><rect x="22" y="26" width="26" height="24" fill="none" stroke="var(--ink)" stroke-width="2"/><path d="M22 33h26" stroke="var(--ink)" stroke-width="2"/></svg>
    <h3>25+ Years of Legal<br>Mastery</h3>
    <p>We have successfully handled thousands of cases, fighting both for and against insurance companies.</p>
    <div class="view-more">View More <svg width="16" height="14" viewBox="0 0 16 14"><path d="M1 7h13M8 1l6 6-6 6" fill="none" stroke="var(--ink)" stroke-width="2.4"/></svg></div>
  </article>
  <article class="abs why-card" style="left:447px">
    <svg class="hex" width="70" height="76" viewBox="0 0 70 76"><polygon points="35,2 67,20 67,56 35,74 3,56 3,20" fill="none" stroke="var(--tan)" stroke-width="3"/><path d="M35 22l13 5v10c0 8-6 13-13 16-7-3-13-8-13-16V27z" fill="none" stroke="var(--tan)" stroke-width="2"/></svg>
    <h3>Extensive Knowledge of<br>Insurance Tactics</h3>
    <p>Having worked for insurance companies, we know their strategies, loopholes, and how to dismantle</p>
    <div class="view-more">View More <svg width="16" height="14" viewBox="0 0 16 14"><path d="M1 7h13M8 1l6 6-6 6" fill="none" stroke="var(--ink)" stroke-width="2.4"/></svg></div>
  </article>
  <article class="abs why-card" style="left:784px">
    <svg class="hex" width="70" height="76" viewBox="0 0 70 76"><polygon points="35,2 67,20 67,56 35,74 3,56 3,20" fill="none" stroke="var(--ink)" stroke-width="3"/><circle cx="26" cy="32" r="4" fill="none" stroke="var(--ink)" stroke-width="2"/><circle cx="44" cy="32" r="4" fill="none" stroke="var(--ink)" stroke-width="2"/><path d="M18 50c0-6 4-9 8-9s8 3 8 9M36 50c0-6 4-9 8-9s8 3 8 9" fill="none" stroke="var(--ink)" stroke-width="2"/></svg>
    <h3>Millions Recovered for<br>Clients</h3>
    <p>Our track record includes life-changing results. A client fell eight feet at a major sporting venue</p>
    <div class="view-more">View More <svg width="16" height="14" viewBox="0 0 16 14"><path d="M1 7h13M8 1l6 6-6 6" fill="none" stroke="var(--ink)" stroke-width="2.4"/></svg></div>
  </article>
</section>

<!-- Strategy -->
<section>
  <h2 class="abs section-title" style="top:2207px">Our Strategy:</h2>
  <div class="abs rule" style="left:574px;top:2254px"></div>
  <p class="abs section-sub mont" style="top:2260px;font-size:24px;font-weight:500">Aggressive, Client-Focused, and Results-Driven</p>

  <div class="abs strat-item" style="top:2332px">
    <svg width="80" height="92" viewBox="0 0 80 92"><polygon points="40,2 78,24 78,68 40,90 2,68 2,24" fill="var(--ink)"/><circle cx="40" cy="44" r="14" fill="none" stroke="#fff" stroke-width="2"/><path d="M40 34v20M30 44h20" stroke="#fff" stroke-width="2"/></svg>
    <h4>Taking on Corporate Giants</h4>
    <p>We don't back down from big insurance companies, property management firms, or major corporations.</p>
  </div>
  <div class="abs strat-divider" style="top:2462px"></div>
  <div class="abs strat-item" style="top:2490px">
    <svg width="80" height="92" viewBox="0 0 80 92"><polygon points="40,2 78,24 78,68 40,90 2,68 2,24" fill="var(--tan)"/><rect x="28" y="30" width="24" height="30" fill="none" stroke="#fff" stroke-width="2"/><path d="M33 38h14M33 45h14M33 52h8" stroke="#fff" stroke-width="2"/></svg>
    <h4>Concierge-Style Legal Care</h4>
    <p>You're not just another case number. We provide dedicated, personalized service, keeping you informed, supported, the legal process.</p>
  </div>
  <div class="abs strat-divider" style="top:2624px"></div>
  <div class="abs strat-item" style="top:2650px">
    <svg width="80" height="92" viewBox="0 0 80 92"><polygon points="40,2 78,24 78,68 40,90 2,68 2,24" fill="var(--ink)"/><circle cx="40" cy="40" r="11" fill="none" stroke="#fff" stroke-width="2"/><path d="M33 49l-4 14 11-5 11 5-4-14" fill="none" stroke="#fff" stroke-width="2"/></svg>
    <h4>No Win, No Fee Guarantee</h4>
    <p>We take your case on a contingency basis, which means you pay nothing unless we win.</p>
  </div>

  <div class="abs" style="left:636px;top:2372px;width:440px;height:352px;border:2px solid var(--tan)"></div>
  <div class="abs" role="img" aria-label="Client signing papers at a reception desk" style="left:650px;top:2359px;width:422px;height:347px;background:linear-gradient(135deg,#3b2a1d,#8a5a32 45%,#c9a27a 75%,#5a3b24)"></div>
</section>

<!-- Practice areas -->
<section>
  <div class="abs practice"></div>
  <h2 class="abs section-title" style="top:2909px">Our Practice Areas</h2>
  <div class="abs rule" style="left:574px;top:2955px"></div>
  <p class="abs section-sub" style="top:2972px;font-size:17px">Comprehensive Representation for the Injured</p>

  <article class="abs pa-card" style="left:110px;top:3023px">
    <svg width="60" height="48" viewBox="0 0 60 48"><path d="M6 34l5-12h24l6 12v8H6z" fill="none" stroke="var(--ink)" stroke-width="2"/><circle cx="15" cy="42" r="4" fill="#fff" stroke="var(--ink)" stroke-width="2"/><circle cx="34" cy="42" r="4" fill="#fff" stroke="var(--ink)" stroke-width="2"/><path d="M44 16l6-6M48 22l8-2" stroke="var(--tan)" stroke-width="2"/></svg>
    <h4>Car Accidents</h4>
    <p>We fight for victims of rear-end crashes, multi-vehicle cyclist accidents, and more.</p>
    <a class="btn">Read More</a>
  </article>
  <article class="abs pa-card" style="left:361px;top:3023px">
    <svg width="60" height="48" viewBox="0 0 60 48"><rect x="18" y="4" width="24" height="42" fill="none" stroke="var(--ink)" stroke-width="2"/><path d="M23 12h4M33 12h4M23 20h4M33 20h4M23 28h4M33 28h4M27 46v-8h6v8" stroke="var(--ink)" stroke-width="2"/></svg>
    <h4>Premises Liability</h4>
    <p>If you were injured due to unsafe conditions at a business, hotel, condo, public</p>
    <a class="btn">Read More</a>
  </article>
  <article class="abs pa-card featured" style="left:612px;top:3023px">
    <svg width="60" height="48" viewBox="0 0 60 48"><circle cx="30" cy="8" r="5" fill="none" stroke="#fff" stroke-width="2"/><path d="M30 14v16M22 22h16M18 46h24v-12H18z" fill="none" stroke="#fff" stroke-width="2"/></svg>
    <h4>Wrongful Death</h4>
    <p>We provide compassionate yet fierce representation families who have lost a loved one due</p>
    <a class="btn">Read More</a>
  </article>
  <article class="abs pa-card" style="left:863px;top:3023px">
    <svg width="60" height="48" viewBox="0 0 60 48"><rect x="16" y="4" width="26" height="38" fill="none" stroke="var(--ink)" stroke-width="2"/><path d="M21 12h16M21 19h16M21 26h10" stroke="var(--ink)" stroke-width="2"/><circle cx="40" cy="38" r="7" fill="#fff" stroke="var(--ink)" stroke-width="2"/></svg>
    <h4>Product Liability</h4>
    <p>If a dangerous product caused your injury, we pursue manufacturers, distributors,</p>
    <a class="btn">Read More</a>
  </article>

  <article class="abs pa-card" style="left:110px;top:3300px">
    <svg width="60" height="48" viewBox="0 0 60 48"><rect x="4" y="18" width="28" height="16" fill="none" stroke="var(--ink)" stroke-width="2"/><path d="M32 22h10l6 8v4H32" fill="none" stroke="var(--ink)" stroke-width="2"/><circle cx="12" cy="38" r="4" fill="#fff" stroke="var(--ink)" stroke-width="2"/><circle cx="40" cy="38" r="4" fill="#fff" stroke="var(--ink)" stroke-width="2"/></svg>
    <h4>Vehicle Accidents</h4>
    <p>Truck accidents often result in devastating injuries. We fight trucking companies insurers</p>
    <a class="btn">Read More</a>
  </article>
  <article class="abs pa-card" style="left:361px;top:3300px">
    <svg width="60" height="48" viewBox="0 0 60 48"><path d="M6 28h48l-8 10H14z" fill="none" stroke="var(--ink)" stroke-width="2"/><path d="M20 28v-10h18l6 10" fill="none" stroke="var(--ink)" stroke-width="2"/><path d="M4 44c6-3 10-3 16 0s10 3 16 0 10-3 18 0" fill="none" stroke="var(--tan)" stroke-width="2"/></svg>
    <h4>Watercraft Accidents</h4>
    <p>From reckless boaters to alcohol-related crashes, we hold negligent parties</p>
    <a class="btn">Read More</a>
  </article>
  <article class="abs pa-card" style="left:612px;top:3300px">
    <svg width="60" height="48" viewBox="0 0 60 48"><circle cx="26" cy="8" r="5" fill="none" stroke="var(--ink)" stroke-width="2"/><path d="M26 14l-4 14 8 6v12M22 28l-8 16M18 20h16" fill="none" stroke="var(--ink)" stroke-width="2"/><path d="M38 36h12l4 6" fill="none" stroke="var(--tan)" stroke-width="2"/></svg>
    <h4>Animal Attacks</h4>
    <p>Florida's strict liability laws mean pet owners responsible for injuries caused by animals.</p>
    <a class="btn">Read More</a>
  </article>
  <article class="abs pa-card" style="left:863px;top:3300px">
    <svg width="60" height="48" viewBox="0 0 60 48"><rect x="10" y="4" width="22" height="18" fill="none" stroke="var(--ink)" stroke-width="2"/><circle cx="38" cy="20" r="4" fill="none" stroke="var(--ink)" stroke-width="2"/><path d="M38 24l-4 12 6 10M36 30l-8 4" fill="none" stroke="var(--ink)" stroke-width="2"/></svg>
    <h4>Workplace Injuries</h4>
    <p>If a third party's negligence contributed to your workplace injury.</p>
    <a class="btn">Read More</a>
  </article>
</section>

<!-- Florida law -->
<section>
  <h2 class="abs section-title" style="top:3747px">Florida Personal Injury Law:</h2>
  <div class="abs rule" style="left:574px;top:3794px"></div>
  <p class="abs section-sub mont" style="top:3806px;font-size:20px;font-weight:500">What You Need to Know</p>

  <article class="abs law-box" style="left:110px;width:300px">
    <div class="law-head">Comparative Negligence<br>(Florida Statutes §768.81)</div>
    <ul class="law-list">
      <li>Even if you were partially at fault, you can still recover compensation.</li>
      <li>Your damages will be reduced based on your percentage of fault.</li>
    </ul>
  </article>
  <article class="abs law-box raised" style="left:451px;width:298px">
    <div class="law-head tan">Statute of Limitations<br>(Florida Statutes §95.11)</div>
    <ul class="law-list tan-dots">
      <li>A personal injury claim and two years for wrongful death cases.</li>
      <li>Missing these deadlines can prevent you from recovering compensation.</li>
    </ul>
  </article>
  <article class="abs law-box" style="left:790px;width:298px">
    <div class="law-head">Premises Liability (Florida<br>Statutes §768.0755)</div>
    <ul class="law-list">
      <li>Property owners are responsible for dangerous conditions they knew or should have known about.</li>
    </ul>
  </article>
</section>

<!-- Call to action -->
<section>
  <div class="abs cta"></div>
  <h2 class="abs cta-title">Take the First Step Toward Justice</h2>
  <p class="abs cta-sub">Let Us Fight for the Compensation You Deserve</p>
  <p class="abs cta-note">If you have been injured due to someone else's negligence, do not wait. Time-sensitive deadlines could impact your case.</p>

  <div class="abs cta-col" style="left:10px">
    <div class="label"><span class="ic"><span><svg width="14" height="14" viewBox="0 0 24 24"><path fill="#fff" d="M6.6 10.8a15 15 0 0 0 6.6 6.6l2.2-2.2a1 1 0 0 1 1-.25 11.4 11.4 0 0 0 3.6.6 1 1 0 0 1 1 1V20a1 1 0 0 1-1 1A17 17 0 0 1 3 4a1 1 0 0 1 1-1h3.5a1 1 0 0 1 1 1c0 1.25.2 2.45.6 3.6a1 1 0 0 1-.25 1z"/></svg></span></span>Call now:</div>
    <div class="value">(305) 555-0182</div>
  </div>
  <div class="abs cta-divider" style="left:393px"></div>
  <div class="abs cta-col" style="left:392px">
    <div class="label"><span class="ic"><span><svg width="14" height="11" viewBox="0 0 18 14"><rect x="1" y="1" width="16" height="12" rx="1.5" fill="none" stroke="#fff" stroke-width="2"/><path d="M1.5 2 9 8l7.5-6" fill="none" stroke="#fff" stroke-width="2"/></svg></span></span>Email:</div>
    <div class="value">hello@darrowinjurylaw.com</div>
  </div>
  <div class="abs cta-divider" style="left:773px"></div>
  <div class="abs cta-col" style="left:742px">
    <div class="label"><span class="ic"><span><svg width="12" height="15" viewBox="0 0 12 16"><path d="M6 15s5-5.5 5-9A5 5 0 0 0 1 6c0 3.5 5 9 5 9z" fill="#fff"/><circle cx="6" cy="6" r="2" fill="var(--tan)"/></svg></span></span>Visit:</div>
    <div class="value">410 Valencia Avenue,<br>Coral Gables, FL 33134</div>
  </div>

  <p class="abs cta-line" style="top:4676px">Free Consultation | No Fees Unless We Win | Aggressive Representation</p>
  <p class="abs cta-line" style="top:4721px">The Darrow Law Firm: Where Justice Meets Dedication.</p>
</section>

<footer class="abs site-footer">©2025.Company Name.All Rights Reserved</footer>

</body>
</html>
```